Wordpress Website for electrician

I'm looking for an easy to maintain website for my electrical contracting business. Need a professional and appealing site.
Im wanting a website where clients can come on and look at services we offer, case studies and advertise our services.
Colours I'm wanting to incorporate are green, white, black and grey
I'm wanting a big slide show on main page where I can place advertising etc.
Menu is to include home, services, our work, specials, energy efficiency and contact
My existing site is www.brivolelectric.com.au
looking for something with a similar layout to this website
Target Market(s)
Businesses
Industry/Entity Type
Electrician
Look and feel

```html
<!DOCTYPE html>
<html lang="en">
<head>
<meta charset="utf-8">
<title>Brivol Connections – Electrical Contractor</title>
<link rel="stylesheet" href="https://fonts.googleapis.com/css2?family=Open+Sans:wght@400;600;700&family=Arimo:wght@400;700&display=swap">
<style>
  :root {
    --green: #3cb044;
    --green-light: #9ccf45;
    --black: #000000;
    --ink: #1a1a1a;
    --text: #555555;
    --grey-line: #cfcfcf;
    --orange: #f29a12;
    --white: #ffffff;
    --footer-icon: #8b8b8b;
  }
  * { margin: 0; padding: 0; box-sizing: border-box; }
  html, body { width: 1124px; height: 1200px; overflow: hidden; background: var(--white); }
  body { position: relative; font-family: "Arimo", Arial, sans-serif; color: var(--text); }
  .abs { position: absolute; }

  .top-strip { left: 0; top: 0; width: 1124px; height: 11px; background: var(--black); }

  /* header */
  .brand { left: 224px; top: 34px; display: flex; align-items: center; gap: 10px; }
  .brand-mark { width: 30px; height: 30px; border-radius: 50%; background: var(--green); }
  .brand-name { font-family: "Open Sans", sans-serif; font-weight: 700; font-size: 22px; color: var(--ink); line-height: 1; }
  .brand-tag { left: 264px; top: 62px; font-size: 9px; color: #888; letter-spacing: .3px; }
  .main-nav { left: 482px; top: 55px; display: flex; gap: 26px; list-style: none; }
  .main-nav li { font-size: 10px; font-weight: 700; color: var(--ink); letter-spacing: .3px; }
  .main-nav li.is-current { color: var(--green); }
  .rule { left: 224px; width: 676px; height: 2px; background: var(--grey-line); }

  /* hero slide */
  .hero-title { left: 246px; font-family: "Open Sans", sans-serif; font-weight: 600; line-height: 1; }
  .hero-green { top: 148px; font-size: 54px; color: var(--green); font-weight: 700; }
  .hero-black { top: 202px; font-size: 56px; color: var(--ink); letter-spacing: -.5px; }
  .hero-art { left: 613px; top: 120px; width: 207px; height: 271px;
    background: radial-gradient(ellipse at 50% 35%, #a9d24f 0%, #bcdc74 45%, #e6f1cf 75%, transparent 78%),
                radial-gradient(ellipse at 50% 100%, #b8db6f 0%, #dcedbf 40%, transparent 42%); }
  .grass { left: 225px; top: 357px; width: 328px; height: 34px; background: linear-gradient(180deg, #6cbd3a, #3f8f24); }
  .slide-bar { left: 249px; top: 326px; width: 311px; height: 31px; background: #111; display: flex; align-items: center; justify-content: space-between; padding: 0 10px; }
  .slide-bar .caption { font-size: 11px; color: #bbb; font-weight: 700; letter-spacing: .2px; }
  .slide-bar .cta { font-size: 11px; color: var(--orange); font-weight: 700; }
  .slide-dots { left: 842px; top: 364px; display: flex; gap: 5px; }
  .slide-dots span { width: 9px; height: 9px; border-radius: 50%; background: var(--black); }
  .slide-dots span.is-active { background: var(--green); }

  /* services */
  .service { width: 230px; text-align: center; top: 437px; }
  .service-icon { width: 80px; height: 80px; border-radius: 50%; background: var(--green); margin: 0 auto; display: flex; align-items: center; justify-content: center; }
  .service h2 { margin-top: 23px; font-size: 14.5px; font-weight: 700; color: var(--green); letter-spacing: .3px; }
  .service p { margin-top: 11px; font-size: 10.5px; line-height: 14px; color: #444; }
  .service a { display: block; font-size: 10.5px; color: var(--orange); text-decoration: none; }

  /* info columns */
  .col { top: 661px; width: 200px; }
  .col-head { display: flex; align-items: center; gap: 10px; font-size: 13px; font-weight: 700; color: var(--ink); padding-bottom: 6px; border-bottom: 4px solid var(--ink); letter-spacing: .3px; }
  .col p, .col li { font-size: 9px; line-height: 13px; color: #666; }
  .col-body { margin-top: 12px; }
  .read { margin-top: 8px; font-size: 9px; font-weight: 700; color: var(--orange); display: flex; gap: 12px; }
  .read b { color: var(--ink); }
  .benefits { list-style: none; }
  .benefits li { display: flex; gap: 8px; margin-bottom: 9px; }
  .tick { flex: none; width: 11px; height: 11px; background: #999; margin-top: 1px; }
  .credit { margin-top: 14px; font-style: italic; }

  /* portfolio */
  .section-head { left: 224px; display: flex; align-items: center; gap: 10px; font-size: 13px; font-weight: 700; color: var(--ink); letter-spacing: .3px; }
  .work { top: 883px; width: 151px; height: 94px; }
  .work .view { position: absolute; right: 0; bottom: 0; background: var(--orange); color: var(--ink); font-size: 9px; font-weight: 700; padding: 3px 6px; }

  /* blog / social */
  .small-head { font-size: 9px; font-weight: 700; color: var(--ink); display: flex; gap: 8px; letter-spacing: .3px; }
  .blog-text { left: 224px; top: 1062px; width: 465px; font-size: 9px; line-height: 14px; color: #666; }
  .connect { left: 747px; top: 1028px; }
  .connect-icons { display: flex; gap: 9px; margin-top: 20px; }
  .connect-icons span { width: 24px; height: 24px; border-radius: 50%; }

  /* footer */
  .site-footer { left: 0; top: 1129px; width: 1124px; height: 71px; background: var(--black); }
  .phone { left: 226px; top: 1153px; display: flex; align-items: center; gap: 8px; color: var(--white); font-size: 20px; font-weight: 700; }
  .footer-social { left: 436px; top: 1155px; display: flex; gap: 16px; }
  .footer-social span { width: 24px; height: 24px; border-radius: 50%; background: var(--footer-icon); }
  .footer-brand { left: 729px; top: 1150px; display: flex; align-items: center; gap: 10px; }
  .footer-brand .brand-mark { background: var(--white); }
  .footer-brand .brand-name { color: var(--white); }
</style>
</head>
<body>
  <div class="abs top-strip"></div>

  <header>
    <div class="abs brand"><span class="brand-mark"></span><span class="brand-name">brivol connections</span></div>
    <div class="abs brand-tag">electrical contractor</div>
    <ul class="abs main-nav">
      <li>HOME</li><li>OURWORK</li><li class="is-current">SERVICES</li><li>SPECIAL</li><li>ENERGYEFFCIENCY</li><li>CONTACT US</li>
    </ul>
  </header>
  <div class="abs rule" style="top:107px"></div>

  <section class="hero">
    <div class="abs hero-title hero-green">BE GREEN</div>
    <div class="abs hero-title hero-black">SAVE MONEY</div>
    <div class="abs hero-art" role="img" aria-label="Illustration of a green tree with dollar-sign leaves growing on a hill"></div>
    <div class="abs grass" role="img" aria-label="Strip of green grass"></div>
    <div class="abs slide-bar"><span class="caption">LED IS THE FUTURE</span><span class="cta">VIEW SPECIAL →</span></div>
    <div class="abs slide-dots"><span></span><span></span><span></span><span class="is-active"></span></div>
  </section>
  <div class="abs rule" style="top:390px"></div>

  <section>
    <div class="abs service" style="left:209px">
      <div class="service-icon">
        <svg width="46" height="46" viewBox="0 0 46 46" fill="none" stroke="#fff" stroke-width="6" stroke-linecap="round"><path d="M14 12a16 16 0 1 0 18 0"/><path d="M23 5v17"/></svg>
      </div>
      <h2>ELECTRICAL CONTRACTING</h2>
      <p>We offer all types of electrical work<br>from installation to maintenance</p>
      <a>VIEW SERVICES</a>
    </div>
    <div class="abs service" style="left:442px">
      <div class="service-icon">
        <svg width="40" height="52" viewBox="0 0 40 52" fill="#fff"><rect x="8" y="4" width="24" height="24" rx="4"/><rect x="12" y="30" width="16" height="5"/><rect x="12" y="37" width="16" height="4"/><rect x="14" y="43" width="12" height="5" rx="2"/></svg>
      </div>
      <h2>ENERGY EFFICIENCY</h2>
      <p>With one of our audits to your business or home<br>we can lower your energy bills and minimise<br>your carbon footprint</p>
      <a>VIEW SERVICES</a>
    </div>
    <div class="abs service" style="left:673px">
      <div class="service-icon">
        <svg width="54" height="54" viewBox="0 0 54 54" fill="none" stroke="#fff" stroke-width="4" stroke-linecap="round"><path d="M34 10l-14 24"/><path d="M28 8l12 6"/><path d="M16 30l8 5-5 9-8-4z" fill="#fff"/><path d="M6 48L48 6"/></svg>
      </div>
      <h2>UNDERGROUND LOCATING</h2>
      <p>We have the tools and knowledge in locating<br>underground utilities</p>
      <a>VIEW SERVICES</a>
    </div>
  </section>

  <section>
    <div class="abs col" style="left:225px">
      <div class="col-head"><span>→</span>NEWS</div>
      <div class="col-body">
        <p>Lorem ipsum dolor sit amet, consectetur adipiscing elit. Pellentesque quis nulla id orci malesuada porta posuere quis massa. Nunc vitae purus non augue scelerisque ultricies vitae et velit. Sed vitae lectus id sem lobortis scelerisque. Praesent eget consequat libero.</p>
        <div class="read"><b>→</b>READ</div>
      </div>
    </div>
    <div class="abs col" style="left:462px">
      <div class="col-head"><span>→</span>OUR BENEFITS</div>
      <ul class="col-body benefits">
        <li><span class="tick"></span><span>Lorem ipsum dolor sit amet, consectetur adipiscing elit. Pellentesque quis nulla id orci malesuada porta posuere quis massa.</span></li>
        <li><span class="tick"></span><span>Nunc vitae purus non augue scelerisque ultricies vitae et velit. Sed vitae lectus id sem lobortis scelerisque. Praesent eget consequat.</span></li>
        <li><span class="tick"></span><span>Lorem ipsum dolor sit amet, consectetur adipiscing elit. Pellentesque quis nulla id orci malesuada porta posuere quis massa.</span></li>
      </ul>
    </div>
    <div class="abs col" style="left:700px">
      <div class="col-head"><span>→</span>TESTIMONIALS</div>
      <div class="col-body">
        <p>Lorem ipsum dolor sit amet, consectetur adipiscing elit. Pellentesque quis nulla id orci malesuada porta posuere quis massa. Nunc vitae purus non augue scelerisque ultricies vitae et velit. Sed vitae lectus id sem lobortis scelerisque.</p>
        <p class="credit">Dana, Northwire Studio</p>
      </div>
    </div>
  </section>

  <div class="abs rule" style="top:843px;height:1px"></div>
  <section>
    <div class="abs section-head" style="top:856px"><span>→</span>OUR PORTFOLIO</div>
    <div class="abs work" style="left:225px;background:linear-gradient(135deg,#c4582a,#6d6a66 60%,#d8d8d8)" role="img" aria-label="Photo of switchgear with orange cabling"><span class="view">VIEW →</span></div>
    <div class="abs work" style="left:400px;background:linear-gradient(180deg,#b9b9b9,#8c8c8c 60%,#7d7a5c)" role="img" aria-label="Photo of an industrial building wall with outdoor units"><span class="view">VIEW →</span></div>
    <div class="abs work" style="left:573px;background:linear-gradient(135deg,#7a3d24,#b9b2a8 50%,#e8e6e2)" role="img" aria-label="Photo of an air conditioning unit against a brick wall"><span class="view">VIEW →</span></div>
    <div class="abs work" style="left:748px;background:linear-gradient(135deg,#2e2e2e,#9a9a9a 55%,#474747)" role="img" aria-label="Photo of a rooftop air conditioning unit"><span class="view">VIEW →</span></div>
  </section>
  <div class="abs rule" style="top:1005px;height:1px"></div>

  <section>
    <div class="abs small-head" style="left:225px;top:1030px"><span>→</span>BLOG UPDATES</div>
    <p class="abs blog-text">Lorem ipsum dolor sit amet, consectetur adipiscing elit. Pellentesque quis nulla id orci malesuada porta posuere quis massa. Nunc vitae purus non augue scelerisque ultricies vitae et velit. Sed vitae lectus id sem lobortis scelerisque. Praesent eget consequat libero.</p>
    <div class="abs connect">
      <div class="small-head"><span>→</span>CONNECT WITH US</div>
      <div class="connect-icons">
        <span style="background:#4fb8e6"></span><span style="background:#3b5a98"></span><span style="background:#c8c8c8"></span><span style="background:#f28b1f"></span>
      </div>
    </div>
  </section>

  <footer>
    <div class="abs site-footer"></div>
    <div class="abs phone">
      <svg width="24" height="24" viewBox="0 0 24 24" fill="none" stroke="#fff" stroke-width="2"><circle cx="12" cy="12" r="10.5"/><path d="M8.5 6.5l2 2.5-1.2 1.5c.8 1.7 2 2.9 3.7 3.7l1.5-1.2 2.5 2-1.3 1.8c-3.8-.6-8-4.8-8.6-8.6z" fill="#fff" stroke="none"/></svg>
      123-456-789
    </div>
    <div class="abs footer-social"><span></span><span></span><span></span><span></span><span></span></div>
    <div class="abs footer-brand"><span class="brand-mark"></span><span class="brand-name">brivol connections</span></div>
  </footer>
</body>
</html>
```